I am looking for a design that represent my gym/ performance facility that says respect the process on it. This images will be a center piece wall for my gym. I want this wall to stand out. This wall has to be clean and professional. This wall has to be Black and white. The gym is for athletes and regular members so the message has to relate to all. Respect the process represents this wall. Please be creative but clean and professional. Feel free to play with black and white body art. The message again should be "Respect The Process"
THE WALL IS 16FT LONG

Target Market(s)

Fitness and Athletes

Font styles to use
Sans Serif

Requirements
Must have
• Respect The Process
• Must all be in Black and white even images if you use them.
• Motivation words or phrases I.e., "Determination, Focus, Discipline,
• Please use famous or legendary athletes quotes.
• words to use:
• Transformation, Power, success, Strength, Commitment, Motivation, No Excuses, No Regrets, Never Give UP, Beast, Results, Dream Big, Consistency, Hard Work, Challenge,Warrior, Sacrifice, Greatness, Legendary, Winning, Zone, Purpose, Fight, Destiny,
• This Quote will stand alone:
• I HATED EVERY MINUTE OF TRAINING,
• BUT I SAID, "DON'T QUIT.
• SUFFER NOW AND LIVE THE REST
• OF YOUR LIFE A CHAMPION."
• -TOBIAS KERRIGAN
• "IF YOU DON'T WANT TO SACRIFICE FOR WHAT YOU WANT
• WHAT YOU WANT BECOMES THE SACRIFICE."
• "EVERYONE HAS THE DESIRE TO WIN, BUT ONLY CHAMPIONS HAVE THE DESIRE TO PREPARE."
• "IT'S ALWAYS SEEMS IMPOSSIBLE UNTIL IT'S DONE."
Nice to have
• It would be nice to have the words in Mustard yellow print as well as the white.T

```html
<!DOCTYPE html>
<html lang="en">
<head>
<meta charset="utf-8">
<title>Respect The Process – Gym Wall</title>
<link rel="stylesheet" href="https://fonts.googleapis.com/css2?family=Archivo+Black&family=Bebas+Neue&family=Jost:ital,wght@1,600&display=swap">
<style>
  :root {
    --page: #ffffff;
    --wall: #000000;
    --headline: #ffffff;
    --mustard: #f7c600;
    --shadow-word: #3b3b3b;
    --quote: #ffffff;
  }
  html, body {
    margin: 0;
    padding: 0;
    width: 1200px;
    height: 2510px;
    overflow: hidden;
    background: var(--page);
  }
  .wall-canvas { display: block; width: 1200px; height: 2510px; }
  .wall-panel { fill: var(--wall); }
  .headline { font-family: "Archivo Black", "Arial Black", sans-serif; fill: var(--headline); }
  .word { font-family: "Bebas Neue", "Oswald", sans-serif; }
  .word--white { fill: var(--headline); }
  .word--mustard { fill: var(--mustard); }
  .word--grey { fill: var(--shadow-word); }
  .quote { font-family: "Jost", "Futura", sans-serif; font-style: italic; font-weight: 600; fill: var(--quote); }
</style>
</head>
<body>
<svg class="wall-canvas" viewBox="0 0 720 1506" xmlns="http://www.w3.org/2000/svg" role="img" aria-label="Respect The Process motivational wall designs">

  <!-- Wall option one -->
  <g class="wall wall--one">
    <rect class="wall-panel" x="20" y="17" width="672" height="588"/>
    <text class="quote" x="352" y="55" font-size="8.5" text-anchor="middle">“If you don’t sacrifice for what you want, what you want becomes the sacrifice.”</text>

    <text class="headline" x="193" y="272" font-size="61" textLength="112" lengthAdjust="spacingAndGlyphs">THE</text>
    <text class="headline" x="193" y="335" font-size="79" textLength="355" lengthAdjust="spacingAndGlyphs">PROCESS</text>
    <text class="word word--white" transform="translate(187,335) rotate(-90)" font-size="31" textLength="107" lengthAdjust="spacingAndGlyphs">RESPECT</text>

    <text class="word word--grey" x="309" y="247" font-size="28" textLength="118" lengthAdjust="spacingAndGlyphs">CONSISTENCY</text>
    <text class="word word--mustard" x="309" y="272" font-size="28" textLength="152" lengthAdjust="spacingAndGlyphs">TRANSFORMATION</text>
    <text class="word word--mustard" x="165" y="362" font-size="30" textLength="145" lengthAdjust="spacingAndGlyphs">DETERMINATION</text>
    <text class="word word--grey" x="165" y="386" font-size="28" textLength="110" lengthAdjust="spacingAndGlyphs">CHALLENGES</text>
    <text class="word word--grey" x="380" y="366" font-size="34" textLength="130" lengthAdjust="spacingAndGlyphs">COMMITMENT</text>
    <text class="word word--mustard" x="350" y="393" font-size="36" textLength="168" lengthAdjust="spacingAndGlyphs">NEVER GIVE UP</text>

    <text class="word word--grey" transform="translate(532,410) rotate(-90)" font-size="16" textLength="65" lengthAdjust="spacingAndGlyphs">SACRIFICE</text>
    <text class="word word--mustard" transform="translate(560,425) rotate(-90)" font-size="26" textLength="85" lengthAdjust="spacingAndGlyphs">DISCIPLINE</text>
    <text class="word word--mustard" transform="translate(587,430) rotate(-90)" font-size="32" textLength="120" lengthAdjust="spacingAndGlyphs">MOTIVATION</text>
    <text class="word word--grey" transform="translate(612,412) rotate(-90)" font-size="28" textLength="87" lengthAdjust="spacingAndGlyphs">HARD WORK</text>
    <text class="word word--grey" transform="translate(636,378) rotate(-90)" font-size="26" textLength="53" lengthAdjust="spacingAndGlyphs">POWER</text>
    <text class="word word--grey" transform="translate(671,355) rotate(-90)" font-size="40" textLength="127" lengthAdjust="spacingAndGlyphs">LEGENDARY</text>
    <text class="word word--grey" transform="translate(640,275) rotate(-90)" font-size="34" textLength="63" lengthAdjust="spacingAndGlyphs">ZONE</text>
    <text class="word word--mustard" x="548" y="307" font-size="32" textLength="89" lengthAdjust="spacingAndGlyphs">WARRIOR</text>
    <text class="word word--mustard" transform="translate(603,275) rotate(-90)" font-size="34" textLength="85" lengthAdjust="spacingAndGlyphs">RESULTS</text>
    <text class="word word--grey" transform="translate(579,270) rotate(-90)" font-size="32" textLength="95" lengthAdjust="spacingAndGlyphs">PORPUSE</text>
    <text class="word word--mustard" transform="translate(548,270) rotate(-90)" font-size="26" textLength="82" lengthAdjust="spacingAndGlyphs">DREAM BIG</text>

    <text class="word word--mustard" transform="translate(66,372) rotate(-90)" font-size="30" textLength="110" lengthAdjust="spacingAndGlyphs">NO EXCUSES</text>
    <text class="word word--grey" transform="translate(95,410) rotate(-90)" font-size="36" textLength="70" lengthAdjust="spacingAndGlyphs">BEAST</text>
    <text class="word word--grey" transform="translate(103,305) rotate(-90)" font-size="36" textLength="75" lengthAdjust="spacingAndGlyphs">FIGHT</text>
    <text class="word word--grey" x="68" y="338" font-size="36" textLength="97" lengthAdjust="spacingAndGlyphs">WINNING</text>
    <text class="word word--grey" transform="translate(118,422) rotate(-90)" font-size="24" textLength="82" lengthAdjust="spacingAndGlyphs">STRENGTH</text>
    <text class="word word--mustard" transform="translate(130,302) rotate(-90)" font-size="36" textLength="90" lengthAdjust="spacingAndGlyphs">SUCCESS</text>
    <text class="word word--mustard" transform="translate(143,410) rotate(-90)" font-size="28" textLength="100" lengthAdjust="spacingAndGlyphs">NO REGRETS</text>
    <text class="word word--grey" transform="translate(160,410) rotate(-90)" font-size="16" textLength="70" lengthAdjust="spacingAndGlyphs">GREATNESS</text>
    <text class="word word--grey" transform="translate(163,305) rotate(-90)" font-size="40" textLength="110" lengthAdjust="spacingAndGlyphs">STAMINA</text>

    <text class="quote" x="310" y="547" font-size="8.5">"I hated every minute of training, but I said 'don't quit. Suffer now</text>
    <text class="quote" x="310" y="561" font-size="8.5">and live the rest of your life a champion."</text>
    <text class="quote" x="660" y="577" font-size="8.5" text-anchor="end">TOBIAS KERRIGAN.</text>
  </g>

  <!-- Wall option two -->
  <g class="wall wall--two">
    <rect class="wall-panel" x="16" y="773" width="682" height="597"/>

    <text class="word word--mustard" x="43" y="882" font-size="36" textLength="135" lengthAdjust="spacingAndGlyphs">CHALLENGES</text>
    <text class="word word--grey" x="42" y="922" font-size="52" textLength="228" lengthAdjust="spacingAndGlyphs">NEVER GIVE UP</text>
    <text class="word word--white" transform="translate(70,1105) rotate(-90)" font-size="42" textLength="170" lengthAdjust="spacingAndGlyphs">RESPECT</text>

    <text class="headline" x="85" y="1000" font-size="97" textLength="185" lengthAdjust="spacingAndGlyphs">THE</text>
    <text class="headline" x="85" y="1105" font-size="135" textLength="570" lengthAdjust="spacingAndGlyphs">PROCESS</text>

    <text class="word word--grey" transform="translate(300,998) rotate(-90)" font-size="38" textLength="113" lengthAdjust="spacingAndGlyphs">STAMINA</text>
    <text class="word word--grey" x="305" y="910" font-size="38" textLength="140" lengthAdjust="spacingAndGlyphs">GREATNESS</text>
    <text class="word word--mustard" x="305" y="940" font-size="32" textLength="140" lengthAdjust="spacingAndGlyphs">CONSISTENCY</text>
    <text class="word word--grey" x="305" y="972" font-size="38" textLength="118" lengthAdjust="spacingAndGlyphs">SACRIFICE</text>
    <text class="word word--mustard" x="305" y="1000" font-size="32" textLength="155" lengthAdjust="spacingAndGlyphs">DETERMINATION</text>
    <text class="word word--grey" transform="translate(492,1000) rotate(-90)" font-size="38" textLength="105" lengthAdjust="spacingAndGlyphs">PORPUSE</text>
    <text class="word word--mustard" transform="translate(521,1000) rotate(-90)" font-size="34" textLength="90" lengthAdjust="spacingAndGlyphs">RESULTS</text>
    <text class="word word--grey" transform="translate(555,1000) rotate(-90)" font-size="38" textLength="65" lengthAdjust="spacingAndGlyphs">ZONE</text>
    <text class="word word--mustard" x="560" y="1003" font-size="34" textLength="90" lengthAdjust="spacingAndGlyphs">SUCCESS</text>
    <text class="word word--grey" transform="translate(680,1138) rotate(-90)" font-size="30" textLength="158" lengthAdjust="spacingAndGlyphs">TRANSFORMATION</text>

    <text class="word word--grey" x="42" y="1138" font-size="44" textLength="95" lengthAdjust="spacingAndGlyphs">POWER</text>
    <text class="word word--mustard" transform="translate(125,1245) rotate(-90)" font-size="32" textLength="105" lengthAdjust="spacingAndGlyphs">DISCIPLINE</text>
    <text class="word word--mustard" transform="translate(160,1235) rotate(-90)" font-size="42" textLength="130" lengthAdjust="spacingAndGlyphs">DREAM BIG</text>
    <text class="word word--grey" x="162" y="1140" font-size="44" textLength="140" lengthAdjust="spacingAndGlyphs">HARD WORK</text>
    <text class="word word--grey" transform="translate(195,1215) rotate(-90)" font-size="40" textLength="70" lengthAdjust="spacingAndGlyphs">FIGHT</text>
    <text class="word word--grey" x="202" y="1170" font-size="40" textLength="102" lengthAdjust="spacingAndGlyphs">WINNING</text>
    <text class="word word--grey" transform="translate(340,1195) rotate(-90)" font-size="44" textLength="87" lengthAdjust="spacingAndGlyphs">BEAST</text>
    <text class="word word--mustard" transform="translate(365,1228) rotate(-90)" font-size="32" textLength="120" lengthAdjust="spacingAndGlyphs">NO REGRETS</text>
    <text class="word word--mustard" x="368" y="1138" font-size="38" textLength="140" lengthAdjust="spacingAndGlyphs">NO EXCUSES</text>
    <text class="word word--grey" x="368" y="1168" font-size="40" textLength="135" lengthAdjust="spacingAndGlyphs">LEGENDARY</text>
    <text class="word word--mustard" x="368" y="1195" font-size="36" textLength="140" lengthAdjust="spacingAndGlyphs">COMMITMENT</text>
    <text class="word word--grey" transform="translate(540,1230) rotate(-90)" font-size="40" textLength="122" lengthAdjust="spacingAndGlyphs">STRENGTH</text>
    <text class="word word--mustard" transform="translate(570,1260) rotate(-90)" font-size="36" textLength="150" lengthAdjust="spacingAndGlyphs">MOTIVATION</text>
    <text class="word word--mustard" x="570" y="1138" font-size="34" textLength="85" lengthAdjust="spacingAndGlyphs">WARRIOR</text>

    <text class="quote" x="320" y="1315" font-size="8.5">"I hated every minute of training, but I said 'don't quit. Suffer now</text>
    <text class="quote" x="320" y="1330" font-size="8.5">and live the rest of your life a champion."</text>
    <text class="quote" x="675" y="1345" font-size="8.5" text-anchor="end">TOBIAS KERRIGAN</text>
  </g>
</svg>
</body>
</html>
```